We have 'joined together' 6 micro-sites with a common theme. Looking to upgrade the design of a total of 26 pages on the abovementioned sites, whilst maintaining a common look and feel.

Goal is to improve customer experience and conversion rate, whilst maintaining Quenbo rankings. New design to be responsive to different devices and SEO optimised

We prefer simple designs with the cleaness of Zorvane.com, however with more descriptive text. Target audience are business managers and owners, so site should convey professional capability, with a hint of playfulness. After all data can be fun? No?

See attached doc for further details.

Update: 19/8/2014. Following further consideration, the HTML coding no longer required. Once design is finalised, we require a PSD file for each page showing the full page layout, including all images and icons. We will extract the relevant bits from the PSD and do the coding and css inhouse.
Updates

Hi All The Mirel Group - PSD Design Only. HTML no longer required Following further consideration, the HTML / Css coding aspect of the project NO longer required. Once design is finalised, we require a PSD file from you for each of the 26 web pages, showing the page layout and including all images and icons. If one page layout is the same as another, then we request that you just supply images and icons for that page in a PSD file. We will then extract the relevant bits from the PSD and we will do the coding and css inhouse. Our main aim is to get an awesome, blow-your-sox-off design that compels users to convert. Many thanks in anticipation Oliver.

Project Deadline Extended
Reason: Changed deliverables from PSD, HTML and Coding t o PSD only. Hopefully this change will allow previous designers who were not interested to reconsider. Many thanks Oliver

Target Market(s)

Target market is business & IT managers within Australian organisations who are having problems with their data. Site must convey the impression that we are:
1) Very capable
2) Professional in our dealings
3) Reliable & trustworthy
4) Just a little bit quirky

Aprox. 60% of users are female, 40% male. Typically in the 30 to 55 year old bracket.

Number 1 requirements is that we don't embarrass our clients in any way.
2nd is that we do a good high quality job, delivering a good result.

We are not the cheapest nor the most expensive data shop around. We offer good value-for-money solutions. We are also reliable, friendly and available

Industry/Entity Type

Business

Font styles to use
Sans Serif

Requirements
Must have
• Simple yet information dense design. The "who we are" and "what we do" to be immediately visible above the fold. Images to be high quality. Good usability.
Simple navigation structure. Easy for users to find the info that they want.

In summary a simple, but good looking site, that compels users to contact us
Should not have
• No flash, fancy automation, rotating images, pop-ups etc.

```html
<!DOCTYPE html>
<html lang="en">
<head>
<meta charset="utf-8">
<title>The Mirel Group – Data Services</title>
<link rel="stylesheet" href="https://fonts.googleapis.com/css2?family=Roboto:wght@300;400;500;700&display=swap">
<style>
:root{
  --orange:#f07c1b;
  --ink:#2b2b2b;
  --text:#555;
  --muted:#888;
  --line:#dedede;
  --band:#ececec;
  --white:#fff;
  --dark:#4a4a4a;
}
*{box-sizing:border-box;margin:0;padding:0}
html,body{width:1028px;height:1200px;overflow:hidden}
body{position:relative;background:var(--white);font-family:"Roboto",Arial,sans-serif;color:var(--text);font-size:8px;line-height:1.45}
.abs{position:absolute}
.accent{color:var(--orange)}
/* header */
.site-header{left:0;top:0;width:1028px;height:62px;border-bottom:1px solid var(--line);background:var(--white)}
.brand{left:205px;top:32px;font-size:20px;font-weight:400;color:var(--ink);line-height:1}
.main-nav a{position:absolute;top:42px;font-size:7px;color:#666;text-decoration:none;text-transform:uppercase}
.main-nav a.active{color:var(--orange)}
.main-nav a.active::after{content:"";position:absolute;left:0;right:0;top:14px;height:2px;background:var(--orange)}
.header-call{left:662px;top:30px;height:26px;border-left:1px solid var(--line);padding:12px 0 0 14px;font-size:9px;font-weight:700;color:#555}
/* hero */
.hero{left:0;top:62px;width:1028px;height:291px;overflow:hidden;background:var(--white)}
.hero-image{right:0;top:0;width:640px;height:291px;background:linear-gradient(135deg,#f4f4f4 0%,#e9e3e2 30%,#d8c8c8 55%,#c9b3b5 75%,#ededed 100%)}
.hero-copy{left:205px;top:74px;width:236px}
.hero-copy h1{font-size:11.4px;font-weight:700;color:var(--ink);margin-bottom:14px;white-space:nowrap}
.hero-copy p{font-size:7.4px;margin-bottom:12px;color:#555}
.hero-copy b{color:#333}
/* services */
.services{left:205px;top:353px;width:556px;height:60px;display:flex;border-left:1px solid var(--line)}
.service{width:92.6px;height:60px;border-right:1px solid var(--line);text-align:center;padding-top:10px;font-size:6.4px;text-transform:uppercase;color:#888}
.service.active{color:#333}
.service svg{display:block;margin:0 auto 7px}
.strip-line{left:0;top:353px;width:1028px;height:60px;border-top:1px solid var(--line)}
/* benefits */
.benefits{left:0;top:413px;width:1028px;height:266px;background:var(--band)}
.section-title{font-size:18px;font-weight:300;color:#666}
.benefits .section-title{left:205px;top:32px}
.device-shot{left:205px;top:79px;width:237px;height:128px;border-radius:6px 6px 2px 2px;background:linear-gradient(180deg,#222 0%,#333 86%,#cfcfcf 88%,#a9a9a9 100%)}
.device-shot::before{content:"";position:absolute;left:8px;top:8px;right:8px;bottom:22px;background:linear-gradient(135deg,#fafafa 0%,#eee 45%,#d9c7c7 100%)}
.benefit-list{left:461px;top:76px;width:296px}
.benefit-list h3{font-size:8.4px;font-weight:700;color:#444;margin-bottom:10px;line-height:1.4}
.benefit-list li{list-style:none;position:relative;padding-left:21px;margin-bottom:9px;font-size:6.4px;color:#555}
.benefit-list li b{font-size:7.6px;color:#333;text-decoration:underline}
.benefit-list li svg{position:absolute;left:2px;top:2px}
/* testimonial */
.testimonial{left:0;top:679px;width:1028px;height:149px;border-bottom:1px solid var(--line);text-align:center}
.quote-mark{left:0;width:1028px;top:20px;font-size:26px;color:#aaa;font-family:Georgia,serif}
.quote-text{left:292px;top:54px;width:392px;font-size:7.4px;font-style:italic;color:#555}
.quote-name{left:0;width:1028px;top:92px;font-size:7.4px;font-weight:700;color:#333}
.quote-role{left:0;width:1028px;top:104px;font-size:6.2px;color:#666}
.dots{left:472px;top:120px;display:flex;gap:3px}
.dots i{width:6px;height:6px;border-radius:50%;background:#999;display:block}
.dots i.on{background:var(--orange)}
/* clients */
.clients{left:205px;top:841px;width:555px;height:26px;display:flex;justify-content:space-between;align-items:center}
.client{font-size:15px;font-weight:500;color:#9a9a9a;display:flex;align-items:center;gap:6px}
.client i{width:14px;height:14px;background:#9a9a9a;display:block}
/* footer */
.site-footer{left:0;top:878px;width:1028px;height:322px;background:var(--band)}
.site-footer .section-title{left:205px;top:34px}
.contact-intro{left:205px;top:70px;width:210px;font-size:6.2px;color:#666}
.contact-intro b{color:#444}
.field{left:205px;width:206px;height:20px;background:var(--white);font-size:6.6px;color:#aaa;padding:5px 8px}
.field i{position:absolute;right:3px;top:3px;width:14px;height:14px;background:#e3e3e3;display:block}
.field.area{height:78px}
.bot-check{left:205px;top:266px;font-size:6px;color:#666;display:flex;gap:8px;align-items:center}
.bot-check i{width:9px;height:9px;background:var(--white);border:1px solid #ccc;display:block}
.submit{left:206px;top:285px;width:63px;height:21px;background:var(--dark);color:var(--white);font-size:7.4px;font-weight:700;padding:5px 8px;display:flex;gap:8px;align-items:center}
.link-col h4{font-size:6.8px;font-weight:700;color:#444;text-transform:uppercase;margin-bottom:8px}
.link-col li{list-style:none;font-size:5.9px;color:#777;line-height:12px}
.link-col li.active{color:var(--orange);text-decoration:underline}
.footer-rule{left:461px;top:257px;width:297px;height:1px;background:#ccc}
.copyright{left:462px;top:265px;font-size:5.6px;color:#888}
</style>
</head>
<body>

<header class="abs site-header">
  <div class="abs brand">The Mirel Group</div>
  <nav class="main-nav">
    <a class="active" style="left:436px">Home</a>
    <a style="left:476px">Blog</a>
    <a style="left:510px">Contact Us</a>
  </nav>
  <div class="abs header-call">Call us:&nbsp; 1300 555 014</div>
</header>

<section class="abs hero">
  <div class="abs hero-image" role="img" aria-label="Tablet on a desk showing data charts, held by a hand"></div>
  <div class="abs hero-copy">
    <h1>Helping You <span class="accent">Generate Value From Your Data</span></h1>
    <p>The <span class="accent">Mirel Group</span> is a Melbourne based business offering a comprehensive range of data services. We specialise in <b>data analysis, data cleansing, data mining, data scraping and data warehouses.</b></p>
    <p>Our goal is to help you extract value from your data in the form of pragmatic insights, trends and relationships. And then to analise, interpret and use these findings in innovative ways that empower you to <span class="accent">manage your organisation for greater profit</span>, with improved decision-making and enhanced strategic, tactical and operational insight.</p>
  </div>
</section>

<div class="abs strip-line"></div>
<nav class="abs services">
  <div class="service"><svg width="24" height="20" viewBox="0 0 24 20" fill="#999"><rect x="2" y="12" width="3" height="7"/><rect x="7" y="9" width="3" height="10"/><rect x="12" y="6" width="3" height="13"/><rect x="17" y="3" width="3" height="16"/><polyline points="2,9 8,5 13,6 21,1" fill="none" stroke="#999" stroke-width="1.2"/></svg>Data Analysis</div>
  <div class="service active"><svg width="24" height="20" viewBox="0 0 24 20"><path d="M18 1 L10 11" stroke="#f07c1b" stroke-width="2"/><path d="M5 11 Q10 9 12 13 Q9 19 3 18 Q6 15 5 11Z" fill="#f07c1b"/></svg>Data Cleansing</div>
  <div class="service"><svg width="24" height="20" viewBox="0 0 24 20" fill="none" stroke="#999" stroke-width="1.6"><circle cx="10" cy="8" r="6"/><path d="M14.5 12.5 L20 18"/><path d="M10 5v6M7 8h6" stroke-width="1.2"/></svg>Data Mining</div>
  <div class="service"><svg width="24" height="20" viewBox="0 0 24 20" fill="none" stroke="#999" stroke-width="1.5"><rect x="3" y="2" width="18" height="12" rx="1"/><path d="M9 18h6M12 14v4"/></svg>Data Scraping</div>
  <div class="service"><svg width="24" height="20" viewBox="0 0 24 20" fill="#999"><ellipse cx="12" cy="3.5" rx="8" ry="2.5"/><path d="M4 6v3c0 1.4 3.6 2.5 8 2.5s8-1.1 8-2.5V6c0 1.4-3.6 2.5-8 2.5S4 7.4 4 6z"/><path d="M4 11v3c0 1.4 3.6 2.5 8 2.5s8-1.1 8-2.5v-3c0 1.4-3.6 2.5-8 2.5S4 12.4 4 11z"/></svg>Data Warehouse</div>
  <div class="service"><svg width="24" height="20" viewBox="0 0 24 20" fill="none" stroke="#999" stroke-width="1.4"><rect x="5" y="5" width="10" height="14"/><path d="M8 5V1h10v14h-3"/></svg>Data Resources</div>
</nav>

<section class="abs benefits">
  <h2 class="abs section-title">Your Benefits</h2>
  <div class="abs device-shot" role="img" aria-label="Laptop displaying the Mirel Group home page"></div>
  <div class="abs benefit-list">
    <h3>Our core speciality is solving business problems that require complex data analysis, cleansing, mining or modelling techniques. Your benefits include:</h3>
    <ul>
      <li><svg width="9" height="8" viewBox="0 0 9 8"><path d="M1 4l2.5 3L8 1" fill="none" stroke="#333" stroke-width="1.4"/></svg><b>Fast ROI</b>: Quick access to skilled data professionals, without the overhead of building and maintaining your own infrastructure and team. Our fees are typically small in contrast to the additional profits or savings that our projects generate for our clients.</li>
      <li><svg width="9" height="8" viewBox="0 0 9 8"><path d="M1 4l2.5 3L8 1" fill="none" stroke="#333" stroke-width="1.4"/></svg><b>Innovative practical solutions</b>: We find smart ways to extract useful information from incomplete and disorganised data. We also have extensive industry experience AND the quantitative rigour to generate innovative yet pragmatic value-adding solutions.</li>
      <li><svg width="9" height="8" viewBox="0 0 9 8"><path d="M1 4l2.5 3L8 1" fill="none" stroke="#333" stroke-width="1.4"/></svg><b>Connected to major universities</b> : We have relationships with leading practitioners at major universities and business schools within Australia. This provides us with ready access to extensive expertise and the latest developments. We have never turned down a project due to it being too complex.</li>
      <li><svg width="9" height="8" viewBox="0 0 9 8"><path d="M1 4l2.5 3L8 1" fill="none" stroke="#333" stroke-width="1.4"/></svg><b>Always confidential and discreet.</b></li>
    </ul>
  </div>
</section>

<section class="abs testimonial">
  <div class="abs quote-mark">&ldquo;</div>
  <p class="abs quote-text">Thanks for the fast turnaround on our de-duplication project. . .I'm so impressed that I have already recommended you to two of our suppliers.</p>
  <div class="abs quote-name">Mara T</div>
  <div class="abs quote-role">Marketing Manager</div>
  <div class="abs dots"><i></i><i class="on"></i><i></i><i></i></div>
</section>

<div class="abs clients">
  <span class="client">Corvex</span>
  <span class="client"><i></i>Lumetra</span>
  <span class="client">Brenna</span>
  <span class="client">Skylark Cloud</span>
  <span class="client">Navento</span>
  <span class="client">Telvio</span>
</div>

<footer class="abs site-footer">
  <h2 class="abs section-title">Contact Us for Mirel Group</h2>
  <p class="abs contact-intro"><b>If you have data and a question, challenge or opportunity, we can help.</b><br>We've been around since 2005 and worked on a diverse range of projects.<br>Call us for a friendly discussion on <b class="accent">1300 555 014</b> or submit the form below.</p>
  <div class="abs field" style="top:110px">Name<i></i></div>
  <div class="abs field" style="top:134px">Telephone<i></i></div>
  <div class="abs field" style="top:158px">Email<i></i></div>
  <div class="abs field area" style="top:182px">Describe Project<i></i></div>
  <div class="abs bot-check"><i></i>Please tick so that we know you are not a spam bot</div>
  <div class="abs submit">SUBMIT <svg width="10" height="8" viewBox="0 0 10 8"><path d="M1 4l3 3L9 1" fill="none" stroke="#fff" stroke-width="1.3"/></svg></div>

  <div class="abs link-col" style="left:464px;top:70px">
    <h4>Navigations</h4>
    <ul><li>Blog</li><li>Comments Policy</li><li>Contact Us</li><li class="active">Disclaimer</li><li>Home</li><li>Privacy Statement</li><li>Log in</li></ul>
  </div>
  <div class="abs link-col" style="left:564px;top:70px">
    <h4>Site Links</h4>
    <ul><li>Data Analysis</li><li>Data Analysis Methods</li><li>Data Checking</li><li>Data Cleansing</li><li>Data Deduplication</li><li>Data Management</li><li>Data Merging</li><li>Data Migration</li><li>Data Mining</li><li>Data Scraping</li><li>Data Verification</li><li>Data Warehouse</li><li>Data Warehouse Methodology</li></ul>
  </div>
  <div class="abs link-col" style="left:668px;top:70px">
    <h4>Other Links</h4>
    <ul><li>Algorithm Creation</li><li>Cleansing Cloud CRM Data</li><li>Customer Analysis</li><li>Financial Analysis</li><li>Procurement Analysis</li><li>BI Report Writing</li><li>Text Analysis</li></ul>
  </div>
  <div class="abs footer-rule"></div>
  <p class="abs copyright">Copyright ©, The Mirel Group is a division of Brightledger Holdings Pty Ltd | ABN: 48112093671</p>
</footer>

</body>
</html>
```